2in1 Bartender & Sommelier needs a business card

I need a business card. I worked as a bartender in many places but I just finished a sommelier school and I would like a new business card. I like minimal design, natural materials and something what makes the people think :) I try to be creative in cocktail making, like little mixology, little twist on recipes... I like to travel and discover new places, cultures and of course interesting drinks and improve continously...live a little bit crazy life. And I like what I do...

Target Market(s)

restaurant/winebar managers, winemakers, other sommeliers and bartenders, people who work in food and beverage sector

Industry/Entity Type

Hospitality

Contact Information for Business Card

Rozsa Tarkany
Bartender & Sommelier
Phone: (FR) +33 6 4827 3190
(HU) +36 70 918 6352

Font styles to use
Script

Requirements
Must have
• Some sign, I am a bartender and sommelier as well.
Nice to have
• black and white maybe with 1 or 2 extra color
Should not have
• very colourful, to many things on the card

```html
<!DOCTYPE html>
<html lang="en">
<head>
<meta charset="utf-8">
<title>Rozsa Tarkany – Bartender &amp; Sommelier</title>
<link href="https://fonts.googleapis.com/css2?family=Bebas+Neue&family=Lobster&family=Lobster+Two&family=Courgette&display=swap" rel="stylesheet">
<style>
  :root {
    --backdrop: #1c1c1c;
    --card: #121212;
    --card-sheen: #262626;
    --white: #f4f4f2;
    --gold: #f0cf6f;
    --gold-deep: #e7bb3c;
  }
  * { margin: 0; padding: 0; box-sizing: border-box; }
  html, body {
    width: 1200px;
    height: 1000px;
    overflow: hidden;
    background: var(--backdrop);
  }
  .business-card {
    position: absolute;
    left: 360px;
    top: 80px;
    width: 480px;
    height: 840px;
    border-radius: 26px;
    background: radial-gradient(ellipse at 60% 40%, var(--card-sheen) 0%, var(--card) 60%);
    overflow: hidden;
    color: var(--white);
  }
  .name-row {
    position: absolute;
    top: 58px;
    left: 0;
    width: 100%;
    display: flex;
    align-items: center;
    justify-content: center;
    gap: 16px;
  }
  .name-rule {
    flex: 0 0 40px;
    height: 4px;
    background: var(--white);
  }
  .holder-name {
    font-family: "Bebas Neue", sans-serif;
    font-size: 66px;
    font-weight: 400;
    line-height: 1;
    letter-spacing: 1px;
    color: var(--white);
    white-space: nowrap;
  }
  .holder-role {
    position: absolute;
    top: 138px;
    left: 80px;
    font-family: "Lobster", cursive;
    font-size: 21px;
    color: var(--gold);
    letter-spacing: 0.5px;
  }
  .services {
    position: absolute;
    top: 186px;
    left: 52px;
    list-style: none;
    font-family: "Lobster Two", cursive;
    font-size: 42px;
    line-height: 1.0;
    color: var(--white);
  }
  .contact-phones {
    position: absolute;
    top: 560px;
    left: 30px;
    font-family: "Courgette", cursive;
    font-size: 17px;
    line-height: 1.7;
    color: var(--white);
    letter-spacing: 0.5px;
    white-space: nowrap;
  }
  .phone-region { margin-left: 4px; }
  .drink-illustration {
    position: absolute;
    left: 262px;
    top: 440px;
    width: 196px;
    height: 356px;
    border-radius: 12px;
    background: radial-gradient(ellipse at 55% 35%, var(--gold) 0%, rgba(240, 207, 111, 0.45) 35%, rgba(244, 244, 242, 0.08) 70%, transparent 85%);
  }
  .bottom-stripe {
    position: absolute;
    left: 0;
    bottom: 18px;
    width: 100%;
    height: 8px;
    background: var(--gold-deep);
  }
</style>
</head>
<body>
  <main class="business-card">
    <div class="name-row">
      <span class="name-rule"></span>
      <h1 class="holder-name">Rozsa Tarkany</h1>
      <span class="name-rule"></span>
    </div>
    <p class="holder-role">Bartender &amp; Sommelier</p>
    <ul class="services">
      <li>cocktail parties</li>
      <li>corporate events</li>
      <li>dinner parties</li>
    </ul>
    <div class="contact-phones">
      <p>+33 6 4827 3190 <span class="phone-region">(FR)</span></p>
      <p>+36 70 918 6352 <span class="phone-region">(HU)</span></p>
    </div>
    <div class="drink-illustration" role="img" aria-label="Martini glass with gold drink and an olive on a pick"></div>
    <div class="bottom-stripe"></div>
  </main>
</body>
</html>
```